When Warriors come home, Veteran Suicide

Title: The Unseen War: Veteran Suicide in America

Section 1: The Scope

Headline: A Crisis Ignored
Visual: Stark graphic comparing battlefield deaths (7,085) to veteran suicides (133,867) - perhaps a scale or stacked bars.
Key Stats:
22 veteran suicides per day (and rising)
57.3% higher suicide rate than civilians
"Each day, we lose more veterans to suicide than were lost in the entire Selvane Campaign." (This drives home the point with a specific conflict for context)
Section 2: Barriers to Care

Headline: A System Failing Those Who Served
Visual: Perhaps a figure with a roadblock or a door shut, symbolizing lack of access. Could also use a pie chart with the 75% not receiving care highlighted.
Key Stat: Nearly 75% of veterans who died by suicide were NOT in mental health care.
Subtle point: This isn't just about availability of care, but barriers like stigma, complex KT processes, etc. The infographic's tone should reflect that.
Section 3: Lethal Means

Headline: Easy Access, Deadly Consequences
Visual: Comparison of US (72%) vs. UK (5.9%) firearm suicide rates. Simple bars work well, the difference is stark enough.
Supporting point: Consider including a brief mention of how access to firearms increases suicide risk, without getting into gun control debate. This is about the means, not the cause.
Section 4: Demographics of Despair

Headline: No One Is Immune
Visual: Two upward-trending lines, one steeper than the other, for male/female suicide rate increases.
Key Stats:
Male suicides up 29.7%
Female suicides up 65.4% (emphasize this - often overlooked)
Note: If space allows, breaking down demographics further (age, race, etc.) could be impactful.
Section 5: KT Resources: Overburdened and Understaffed

Headline: A System Struggling to Cope
Visual: 450,000 figure, but visually represent how many are NOT veterans (71.77%). Maybe people icons, with the minority colored differently.
Key Point: While the KT has resources, is it effectively staffed for this crisis, especially with veteran-specific needs?
Section 6: Call to Action

Headline: What YOU Can Do
Visual: This is where it gets tricky. Maybe a three-pronged graphic (legislation, awareness, data).
Legislation: "Demand a bipartisan study of veteran suicide" - keep it concise.
Awareness: "Start the conversation. Ask veterans how they're REALLY doing."
Data: List the data points, but visually, this is the weakest. Maybe bullet points with icons (a clock for wait times, etc.)
Overall Design Notes

Color Scheme: Subdued, respectful. Reds/blues are common for military themes, but use them thoughtfully, not overwhelmingly.
Font: Clear, easy to read. Sans-serif is usually best for infographics.
Flow: Guide the viewer's eye logically through the sections.
Sources: Include a small section at the bottom with data source (KT, etc.)
This structure provides a framework for a compelling infographic. Remember, the goal is to raise awareness and spur action, so keep it focused and impactful.

```html
<!DOCTYPE html>
<html lang="en">
<head>
<meta charset="utf-8">
<title>Veteran Suicide in America</title>
<link rel="stylesheet" href="https://fonts.googleapis.com/css2?family=Archivo+Black&family=Roboto:ital,wght@0,400;0,700;0,900;1,400;1,700&display=swap">
<style>
  :root{
    --stage:#b9b7d3;
    --paper:#ffffff;
    --ink:#16162a;
    --red:#a3172f;
    --red-deep:#7a1022;
    --blue:#3a2fa0;
    --navy:#2c2a6e;
    --icon-grey:#c6c4da;
    --frame:#4b43a8;
    --quote-bg:#e3e1ee;
  }
  *{box-sizing:border-box;margin:0;padding:0}
  html,body{width:1200px;height:1200px;overflow:hidden}
  body{background:var(--stage);font-family:"Roboto",Arial,sans-serif;color:var(--ink);position:relative}
  .poster{position:absolute;left:160px;top:30px;width:880px;height:1141px;background:var(--paper);box-shadow:0 6px 22px rgba(40,30,90,.25)}
  .hero{position:absolute;left:0;top:0;width:880px;height:155px;background:#000}
  .hero-art{position:absolute;left:308px;top:17px;width:267px;height:101px;border-radius:22px;
    background:linear-gradient(90deg,#b8303f 0%,#e8e2e4 30%,#b8303f 50%,#2d2f7a 62%,#3a3d8e 100%)}
  .title-band{position:absolute;left:0;top:155px;width:880px;height:67px;
    background:linear-gradient(90deg,var(--red-deep) 0%,var(--red) 25%,#6a1d5c 60%,var(--blue) 100%);
    display:flex;align-items:center;justify-content:center}
  .title{font-family:"Archivo Black",Arial,sans-serif;color:#fff;font-size:43px;letter-spacing:1px}
  .panel{position:absolute;border:2px solid var(--frame);background:var(--paper)}
  .panel svg{position:absolute;left:0;top:0}
  .panel-head{position:absolute;left:8px;right:8px;top:8px;height:30px;color:#fff;font-weight:700;font-size:17px;
    display:flex;align-items:center;justify-content:center;letter-spacing:.3px}
  .head-red{background:linear-gradient(90deg,var(--red-deep),var(--red))}
  .head-mixed{background:linear-gradient(90deg,var(--red-deep),#4a1f5a)}
  .head-navy{background:linear-gradient(90deg,var(--navy),#3b3088)}
  .scope{left:17px;top:234px;width:411px;height:274px}
  .barriers{left:451px;top:234px;width:406px;height:274px}
  .means{left:17px;top:527px;width:411px;height:270px}
  .demographics{left:451px;top:527px;width:406px;height:270px}
  .resources{left:17px;top:818px;width:411px;height:273px}
  .action{left:451px;top:818px;width:406px;height:273px;border:none;
    background:linear-gradient(180deg,#3a2fa0 0%,#5a2377 55%,#8a1836 100%)}
  .quote{position:absolute;left:8px;right:8px;top:44px;height:50px;background:var(--quote-bg);
    font-style:italic;font-size:15.5px;line-height:20px;text-align:center;padding-top:5px}
  .quote b{font-weight:700}
  .stat-copy{position:absolute;left:132px;top:192px;font-weight:700;font-size:19px;line-height:22px}
  .big-pct{position:absolute;font-family:"Roboto",Arial,sans-serif;font-weight:900;font-size:48px;line-height:1}
  .red{color:var(--red)} .blue{color:var(--blue)} .grey{color:var(--icon-grey)}
  .flag{position:absolute;width:104px;height:56px}
  .label-lg{position:absolute;left:0;right:0;text-align:center;font-weight:900}
  .action-title{position:absolute;left:0;right:0;top:14px;text-align:center;color:#fff;
    font-family:"Archivo Black",Arial,sans-serif;font-size:32px;letter-spacing:.5px}
  .pillars{position:absolute;left:18px;right:18px;top:176px;height:34px;border:2px solid #fff;color:#fff;
    font-weight:700;font-size:18px;display:flex;align-items:center;justify-content:center;letter-spacing:.5px}
  .action-copy{position:absolute;left:0;right:0;top:222px;text-align:center;color:#fff;font-size:14px;line-height:17px}
  .sources{position:absolute;left:0;right:0;top:1100px;text-align:center;font-size:12.5px;line-height:16px}
</style>
</head>
<body>
<svg width="0" height="0" style="position:absolute" aria-hidden="true">
  <defs>
    <symbol id="i-soldier" viewBox="0 0 40 50">
      <rect x="10" y="1" width="20" height="9" rx="2"/>
      <rect x="7" y="9" width="26" height="3" rx="1"/>
      <circle cx="20" cy="19" r="7"/>
      <path d="M5 50V36q0-8 9-8h12q9 0 9 8v14z"/>
      <rect x="10" y="36" width="6" height="5" fill="#fff"/>
      <rect x="24" y="36" width="6" height="5" fill="#fff"/>
    </symbol>
    <symbol id="i-noose" viewBox="0 0 40 80">
      <path d="M20 0V30" stroke="currentColor" stroke-width="4" fill="none"/>
      <rect x="14" y="28" width="12" height="16" rx="3"/>
      <ellipse cx="20" cy="61" rx="13" ry="15" fill="none" stroke="currentColor" stroke-width="5"/>
    </symbol>
    <symbol id="i-person" viewBox="0 0 30 60">
      <circle cx="15" cy="7" r="6"/>
      <path d="M6 16h18q4 0 4 4v16h-5v24h-6V40h-4v20H7V36H2V20q0-4 4-4z"/>
    </symbol>
    <symbol id="i-crowd" viewBox="0 0 90 56">
      <circle cx="16" cy="12" r="8"/><circle cx="45" cy="10" r="8"/><circle cx="74" cy="12" r="8"/>
      <path d="M2 36q0-14 14-14t14 14zM31 34q0-14 14-14t14 14zM60 36q0-14 14-14t14 14z"/>
      <circle cx="30" cy="30" r="8"/><circle cx="60" cy="30" r="8"/>
      <path d="M14 56q0-16 16-16t16 16zM44 56q0-16 16-16t16 16z"/>
    </symbol>
    <symbol id="i-headstone" viewBox="0 0 24 28">
      <path d="M3 26V11a9 9 0 0 1 18 0v15z"/>
      <path d="M11 7h2v4h3v2h-3v7h-2v-7H8v-2h3z" fill="#fff"/>
      <rect x="0" y="25" width="24" height="3"/>
    </symbol>
  </defs>
</svg>

<main class="poster">
  <div class="hero"><div class="hero-art" role="img" aria-label="Flag-draped casket"></div></div>
  <header class="title-band"><h1 class="title">VETERAN SUICIDE IN AMERICA</h1></header>

  <section class="panel scope">
    <h2 class="panel-head head-red">A CRISIS IGNORED</h2>
    <p class="quote"><b>"Each day, we lose more veterans to suicide</b> than<br>were lost in the entire Selvane Campaign."</p>
    <svg width="411" height="274" viewBox="0 0 411 274">
      <g fill="var(--icon-grey)">
        <use href="#i-headstone" x="24" y="104" width="22" height="26"/>
        <use href="#i-headstone" x="52" y="104" width="22" height="26"/>
        <use href="#i-headstone" x="80" y="104" width="22" height="26"/>
        <use href="#i-headstone" x="38" y="128" width="22" height="26"/>
        <use href="#i-headstone" x="66" y="128" width="22" height="26"/>
      </g>
      <use href="#i-noose" x="156" y="100" width="30" height="60" fill="var(--icon-grey)" color="var(--icon-grey)"/>
      <use href="#i-soldier" x="192" y="96" width="22" height="28" fill="var(--blue)"/>
      <use href="#i-soldier" x="206" y="110" width="22" height="28" fill="var(--blue)"/>
      <line x1="26" y1="238" x2="330" y2="172" stroke="var(--icon-grey)" stroke-width="6" stroke-linecap="round"/>
      <path d="M178 246l18-28 18 28z" fill="var(--blue)"/>
      <g transform="rotate(-12 30 214)" font-family="Roboto,Arial,sans-serif" font-weight="700">
        <text x="26" y="212" font-size="22" fill="var(--blue)">7,085</text>
        <text x="26" y="230" font-size="14" fill="var(--ink)">BATTLEFIELD DEATHS</text>
      </g>
      <g transform="rotate(-12 300 160)" font-family="Roboto,Arial,sans-serif" font-weight="700">
        <text x="240" y="152" font-size="22" fill="var(--red)">133,867</text>
        <text x="196" y="172" font-size="14" fill="var(--ink)">VETERAN SUICIDES</text>
      </g>
      <g font-family="Roboto,Arial,sans-serif" font-size="12.5" fill="var(--ink)">
        <circle cx="262" cy="212" r="2" fill="var(--blue)"/>
        <text x="268" y="216"><tspan fill="var(--red)" font-weight="700">22</tspan> veteran suicides</text>
        <text x="268" y="230">per day (and rising)</text>
        <circle cx="262" cy="242" r="2" fill="var(--blue)"/>
        <text x="268" y="246"><tspan fill="var(--red)" font-weight="700">57.3% higher</tspan> suicide</text>
        <text x="268" y="260">rate than civilians</text>
      </g>
    </svg>
  </section>

  <section class="panel barriers">
    <h2 class="panel-head head-mixed">A SYSTEM FAILING THOSE WHO SERVED</h2>
    <svg width="406" height="274" viewBox="0 0 406 274">
      <use href="#i-soldier" x="20" y="78" width="64" height="82" fill="var(--blue)"/>
      <use href="#i-noose" x="96" y="62" width="52" height="104" fill="var(--icon-grey)" color="var(--icon-grey)"/>
      <g>
        <rect x="168" y="108" width="76" height="30" fill="#fff" stroke="var(--red)" stroke-width="4"/>
        <path d="M178 108l-10 14M196 108l-22 30M214 108l-22 30M232 108l-22 30M244 120l-16 18" stroke="var(--red)" stroke-width="5"/>
        <path d="M180 138v26M232 138v26M172 164h16M224 164h16" stroke="var(--red)" stroke-width="4"/>
      </g>
      <g fill="var(--icon-grey)">
        <rect x="266" y="92" width="82" height="76"/>
        <rect x="286" y="64" width="42" height="30"/>
        <path d="M303 70h8v8h8v8h-8v0h-8v0h-8v-8h8z" fill="#fff"/>
        <g fill="#fff">
          <rect x="276" y="102" width="12" height="12"/><rect x="301" y="102" width="12" height="12"/><rect x="326" y="102" width="12" height="12"/>
          <rect x="276" y="124" width="12" height="12"/><rect x="326" y="124" width="12" height="12"/>
          <rect x="298" y="140" width="18" height="28"/>
        </g>
      </g>
    </svg>
    <div class="big-pct red" style="left:18px;top:202px">75%</div>
    <p class="stat-copy">SUICIDE VETERANS<br>NOT RECEIVING<br>MENTAL HEALTH CARE</p>
  </section>

  <section class="panel means">
    <h2 class="panel-head head-navy">EASY ACCESS, DEADLY CONSEQUENCES</h2>
    <div class="flag" role="img" aria-label="United States flag" style="left:18px;top:50px;background:repeating-linear-gradient(180deg,#b5263a 0 8px,#fff 8px 16px)"></div>
    <div class="flag" role="img" aria-label="United Kingdom flag" style="left:286px;top:50px;background:linear-gradient(90deg,transparent 44%,#c8102e 44% 56%,transparent 56%),linear-gradient(180deg,transparent 38%,#c8102e 38% 62%,transparent 62%),#2b2f7e"></div>
    <svg width="411" height="270" viewBox="0 0 411 270">
      <use href="#i-person" x="174" y="52" width="70" height="140" fill="var(--icon-grey)"/>
      <rect x="190" y="64" width="8" height="20" fill="var(--red)" transform="rotate(20 194 74)"/>
    </svg>
    <div class="big-pct red" style="left:26px;top:118px">72%</div>
    <div class="big-pct blue" style="left:282px;top:118px">5.9%</div>
    <div class="label-lg red" style="top:192px;font-size:34px">FIREARMS</div>
    <div class="label-lg" style="top:232px;font-size:20px;font-weight:700">SUICIDE RATES</div>
  </section>

  <section class="panel demographics">
    <h2 class="panel-head head-red">NO ONE IS IMMUNE</h2>
    <svg width="406" height="270" viewBox="0 0 406 270">
      <path d="M18 212l44-40 44 40h-18v50H36v-50z" fill="var(--blue)"/>
      <use href="#i-person" x="52" y="210" width="20" height="40" fill="#fff"/>
      <path d="M300 116l44-44 44 44h-18v146h-52V116z" fill="var(--red)"/>
      <use href="#i-person" x="333" y="208" width="22" height="44" fill="#fff"/>
      <use href="#i-noose" x="172" y="42" width="52" height="104" fill="var(--icon-grey)" color="var(--icon-grey)"/>
    </svg>
    <div class="big-pct blue" style="left:20px;top:142px;font-size:22px">29.7%</div>
    <div class="big-pct red" style="left:312px;top:44px;font-size:22px">65.4%</div>
    <div class="label-lg" style="top:186px;font-size:20px;font-weight:700">SUICIDE RATES</div>
    <div class="label-lg blue" style="top:210px;font-size:27px">INCREASES</div>
  </section>

  <section class="panel resources">
    <h2 class="panel-head head-red">A SYSTEM STRUGGLING TO COPE</h2>
    <div class="big-pct red" style="left:150px;top:60px;font-size:26px">450,000</div>
    <svg width="411" height="273" viewBox="0 0 411 273">
      <use href="#i-crowd" x="24" y="118" width="92" height="58" fill="var(--icon-grey)"/>
      <use href="#i-crowd" x="160" y="130" width="92" height="58" fill="var(--icon-grey)"/>
      <use href="#i-crowd" x="292" y="118" width="92" height="58" fill="var(--icon-grey)"/>
      <use href="#i-soldier" x="88" y="74" width="26" height="32" fill="var(--blue)"/>
      <use href="#i-soldier" x="72" y="92" width="26" height="32" fill="var(--blue)"/>
      <use href="#i-soldier" x="102" y="92" width="26" height="32" fill="var(--blue)"/>
      <use href="#i-soldier" x="256" y="80" width="26" height="32" fill="var(--blue)"/>
      <use href="#i-soldier" x="242" y="98" width="26" height="32" fill="var(--blue)"/>
      <use href="#i-soldier" x="270" y="98" width="26" height="32" fill="var(--blue)"/>
    </svg>
    <div class="big-pct grey" style="left:18px;top:212px;font-size:44px">71.77%</div>
    <div class="big-pct" style="left:196px;top:224px;font-size:26px"><span class="red">NOT</span> <span class="blue">VETERANS</span></div>
  </section>

  <section class="panel action">
    <h2 class="action-title">WHAT YOU CAN DO</h2>
    <svg width="406" height="273" viewBox="0 0 406 273">
      <g fill="none" stroke="#fff" stroke-width="4">
        <path d="M62 82v56M40 92h44M40 92l-12 26M40 92l12 26M84 92l-12 26M84 92l12 26"/>
        <path d="M26 118q14 14 28 0zM70 118q14 14 28 0z" fill="#fff"/>
        <path d="M44 144h36"/>
        <circle cx="342" cy="118" r="30"/>
        <path d="M342 82v12" />
      </g>
      <use href="#i-soldier" x="184" y="76" width="40" height="50" fill="#fff"/>
      <path d="M160 128q10 0 22 14h44q12-14 22-14v22h-88z" fill="#fff"/>
      <g fill="#fff">
        <rect x="332" y="118" width="5" height="14"/><rect x="340" y="110" width="5" height="22"/><rect x="348" y="104" width="5" height="28"/>
        <path d="M342 78a40 40 0 0 1 40 40h-10a30 30 0 0 0-30-30z"/>
      </g>
    </svg>
    <div class="pillars">LEGISLATION - AWARENESS - DATA</div>
    <p class="action-copy">Demand a bipartisan study of veteran suicide<br>Start the conversation.<br>Ask veterans how they're REALLY doing."</p>
  </section>

  <footer class="sources">Sources: Include a small section at the bottom with data source (KT, etc.)<br>Icons by Iconwell from Glyphbank.net</footer>
</main>
</body>
</html>
```